Help designing a web admin portal for cloud access control company

Hello, we need help to design our web admin portal for our cloud based access control product called havenpost locks. Please see the attached admin portal wireframe. this is not absolute so we are open to UX / UI suggestions. This web admin portal will allow a admin at a small to medium sized business add new employees to their access control system and grant different access.
Updates

Project Deadline Extended
Reason: Waiting in a couple designs for people that said they would send something in

Target Market(s)

B2B

Industry/Entity Type

It Company

Font styles to use
Sans Serif

Colors
3277b5

Requirements
Must have
• Very simple and clean design. we like clean fonts like Oswald extra light. Please see an image of the wining app designs to see what the color and styling should look like

```html
<!DOCTYPE html>
<html lang="en">
<head>
<meta charset="utf-8">
<title>Havenpost Locks — Dashboard</title>
<link rel="stylesheet" href="https://fonts.googleapis.com/css2?family=Oswald:wght@200;300&family=Lato:wght@400;700&display=swap">
<style>
  :root{
    --topbar:#2347b5;
    --sidebar:#0c1a50;
    --main:#020b26;
    --active:#c8102e;
    --bar:#2347b5;
    --accent-green:#4f9e0a;
    --link:#7f9cff;
    --muted:#b7c0d6;
    --white:#ffffff;
    --card-text:#8a93a8;
    --ink:#1d2233;
    --danger:#d42020;
    --off:#ff3b3b;
    --on:#6fe01a;
  }
  *{box-sizing:border-box;margin:0;padding:0}
  html,body{width:1200px;height:853px;overflow:hidden;background:var(--main);font-family:'Lato',sans-serif;color:var(--white)}
  .app{position:relative;width:1200px;height:853px;overflow:hidden;background:var(--main)}
  .brand{position:absolute;left:0;top:0;width:183px;height:67px;background:var(--topbar);display:flex;align-items:center;justify-content:center;font-family:'Oswald',sans-serif;font-weight:300;font-size:13px;letter-spacing:2.5px}
  .topbar{position:absolute;left:183px;top:0;width:1017px;height:67px;background:var(--topbar)}
  .door-intro{position:absolute;left:45px;top:19px;font-size:10px}
  .door-intro strong{display:block;font-weight:700;margin-bottom:6px}
  .door-intro span{color:var(--link)}
  .door{position:absolute;top:19px;font-size:10px}
  .door strong{display:block;font-weight:700;margin-bottom:6px}
  .door .state{display:flex;align-items:center;gap:5px;color:var(--link)}
  .door .state.open{color:var(--on)}
  .switch{width:24px;height:11px;border-radius:6px;background:#0a1440;position:relative}
  .switch::before{content:"";position:absolute;left:3px;top:3px;width:5px;height:5px;border-radius:50%;background:var(--off)}
  .switch.on::before{left:16px;background:var(--on)}
  .sidebar{position:absolute;left:0;top:67px;width:183px;height:786px;background:var(--sidebar)}
  .user{position:absolute;left:17px;top:16px;display:flex;gap:10px}
  .avatar{width:24px;height:24px;border-radius:50%;background:radial-gradient(circle at 40% 40%,#6f8fd8,#1d3b8f)}
  .user p{font-size:12px;line-height:18px}
  .user a{color:var(--link);text-decoration:none}
  .nav{position:absolute;top:98px;left:0;width:183px;list-style:none}
  .nav li{height:33.3px;line-height:33.3px;padding-left:17px;font-size:12px}
  .nav li.active{background:var(--active)}
  .today{position:absolute;left:17px;bottom:41px;font-size:9.5px;color:var(--muted)}
  .page-title{position:absolute;left:227px;top:108px;font-family:'Oswald',sans-serif;font-weight:200;font-size:31px;letter-spacing:1px}
  .rule{position:absolute;left:227px;top:157px;width:928px;height:1px;background:#162a63}
  .stat{position:absolute;top:190px;width:160px;margin-left:-80px;text-align:center}
  .stat b{display:block;font-family:'Oswald',sans-serif;font-weight:200;font-size:56px;line-height:66px}
  .stat span{display:block;margin-top:11px;font-size:13.5px;color:var(--muted)}
  .chart{position:absolute;left:227px;top:333px}
  .card{position:absolute;background:var(--white);color:var(--ink)}
  .card h3{font-weight:400;font-size:13px;color:var(--card-text);text-align:center;margin-top:14px}
  .status-ring{position:absolute;left:10px;top:45px}
  .status-info{position:absolute;left:94px;top:55px;font-size:9.5px;line-height:12.5px;width:105px}
  .status-info .pct{color:var(--accent-green);font-weight:700}
  .status-info .rate{color:#c5cad6}
  .login-date{text-align:center;font-size:12px;margin-top:45px}
  .forced{text-align:center;font-family:'Oswald',sans-serif;font-weight:200;font-size:58px;color:var(--danger);line-height:1;margin-top:14px}
  .table-card h3{padding-bottom:15px;border-bottom:1px solid #e2e5ec}
  table{border-collapse:collapse;width:100%;font-size:9.5px}
  th{font-weight:700;text-align:left;height:36px;border-bottom:1px solid #eef0f4}
  td{height:16.3px}
  th:first-child,td:first-child{padding-left:17.5px;width:238px}
  th:nth-child(2),td:nth-child(2){width:103px}
  tbody tr:first-child td{padding-top:8px;height:24px}
  .active-state{color:var(--accent-green)}
</style>
</head>
<body>
<div class="app">
  <div class="brand">HAVENPOST LOCKS</div>
  <header class="topbar">
    <div class="door-intro"><strong>Manual Door Opening</strong><span>Toggle the switch to open/close the door</span></div>
    <div class="door" style="left:282px"><strong>Main door</strong><div class="state"><i class="switch"></i>Closed</div></div>
    <div class="door" style="left:365px"><strong>Back door</strong><div class="state"><i class="switch"></i>Closed</div></div>
    <div class="door" style="left:449px"><strong>Exec office</strong><div class="state open"><i class="switch on"></i>Opened</div></div>
    <div class="door" style="left:537px"><strong>Storage room</strong><div class="state"><i class="switch"></i>Closed</div></div>
  </header>

  <aside class="sidebar">
    <div class="user">
      <div class="avatar" role="img" aria-label="User profile photo"></div>
      <p>Welcome Dana!<br><a href="#">Logout</a></p>
    </div>
    <ul class="nav">
      <li>HOME</li><li class="active">DASHBOARD</li><li>CONTROLLER</li><li>DOORS</li><li>EMPLOYEES</li><li>OPEN/CLOSE TIMES</li><li>CAMERAS</li><li>TIME CARD</li><li>REPORT</li><li>SETTINGS</li>
    </ul>
    <div class="today">Today, 30 November 2016</div>
  </aside>

  <h1 class="page-title">DASHBOARD</h1>
  <div class="rule"></div>

  <div class="stat" style="left:296px"><b>24</b><span>Employees</span></div>
  <div class="stat" style="left:454px"><b>20</b><span>Mobile access</span></div>
  <div class="stat" style="left:612px"><b>74</b><span>Cards opens today</span></div>
  <div class="stat" style="left:770px"><b>675</b><span>Cards opens month</span></div>
  <div class="stat" style="left:928px"><b>43</b><span>Mobile opens today</span></div>
  <div class="stat" style="left:1087px"><b>345</b><span>Mobile opens month</span></div>

  <svg class="chart" width="928" height="175" viewBox="272 400 1114 210" aria-label="Door openings chart">
    <g fill="var(--bar)">
      <rect x="314" y="491" width="26" height="116"/><rect x="346" y="481" width="26" height="126"/>
      <rect x="379" y="458" width="26" height="149"/><rect x="411" y="512" width="26" height="95"/>
      <rect x="443" y="528" width="26" height="79"/><rect x="476" y="491" width="26" height="116"/>
      <rect x="508" y="481" width="26" height="126"/><rect x="540" y="441" width="26" height="166"/>
      <rect x="573" y="458" width="26" height="149"/>
      <rect x="605" y="418" width="26" height="189" fill="var(--accent-green)"/>
      <rect x="637" y="481" width="26" height="126"/><rect x="670" y="458" width="26" height="149"/>
      <rect x="702" y="458" width="26" height="149"/><rect x="734" y="431" width="26" height="176"/>
      <rect x="767" y="441" width="26" height="166"/><rect x="799" y="469" width="26" height="138"/>
      <rect x="831" y="491" width="26" height="116"/><rect x="864" y="514" width="26" height="93"/>
      <rect x="896" y="528" width="26" height="79"/><rect x="928" y="545" width="26" height="62"/>
      <rect x="961" y="528" width="26" height="79"/><rect x="993" y="514" width="26" height="93"/>
      <rect x="1025" y="555" width="26" height="52"/><rect x="1058" y="545" width="26" height="62"/>
      <rect x="1090" y="528" width="26" height="79"/><rect x="1122" y="491" width="26" height="116"/>
      <rect x="1155" y="458" width="26" height="149"/><rect x="1187" y="469" width="26" height="138"/>
      <rect x="1219" y="441" width="26" height="166"/><rect x="1252" y="458" width="26" height="149"/>
      <rect x="1284" y="514" width="26" height="93"/><rect x="1317" y="545" width="26" height="62"/>
    </g>
    <rect x="272" y="606" width="1114" height="2" fill="var(--white)"/>
    <rect x="638" y="418" width="98" height="39" fill="var(--white)"/>
    <text x="644" y="431" font-size="9" fill="#9aa0ad" font-family="Lato,sans-serif">Label</text>
    <text x="644" y="447" font-size="9" fill="#1d2233" font-family="Lato,sans-serif">var x <tspan fill="var(--accent-green)">149</tspan>, var y <tspan fill="var(--accent-green)">20</tspan></text>
  </svg>

  <section class="card" style="left:227px;top:561px;width:215px;height:133px">
    <h3>Server status</h3>
    <svg class="status-ring" width="70" height="70" viewBox="0 0 70 70"><circle cx="35" cy="35" r="29" fill="none" stroke="var(--accent-green)" stroke-width="7"/><text x="35" y="44" text-anchor="middle" font-family="Oswald,sans-serif" font-weight="200" font-size="24" fill="var(--ink)">Up</text></svg>
    <div class="status-info">Server uptime (past 6 hours)<br><span class="pct">100%</span><br><span class="rate">Response rate 1ms</span></div>
  </section>

  <section class="card" style="left:465px;top:561px;width:215px;height:133px">
    <h3>Mobile status</h3>
    <svg class="status-ring" width="70" height="70" viewBox="0 0 70 70"><circle cx="35" cy="35" r="29" fill="none" stroke="var(--accent-green)" stroke-width="7"/><text x="35" y="44" text-anchor="middle" font-family="Oswald,sans-serif" font-weight="200" font-size="24" fill="var(--ink)">Up</text></svg>
    <div class="status-info">Mobile uptime (past 6 hours)<br><span class="pct">98.2%</span><br><span class="rate">Response rate 1.2ms</span></div>
  </section>

  <section class="card" style="left:227px;top:719px;width:215px;height:134px">
    <h3>Last login</h3>
    <p class="login-date">30 November 2016 at 3:20pm</p>
  </section>

  <section class="card" style="left:465px;top:719px;width:215px;height:134px">
    <h3>Forced opening</h3>
    <p class="forced">3</p>
  </section>

  <section class="card table-card" style="left:702px;top:561px;width:452px;height:292px">
    <h3>Table List</h3>
    <table>
      <thead><tr><th>Employee name</th><th>Logged in</th><th>Logged out</th></tr></thead>
      <tbody>
        <tr><td>Owen Brackley</td><td>4:32 PM</td><td class="active-state">Still active</td></tr>
        <tr><td>Lena Marsh</td><td>3:20 PM</td><td class="active-state">Still active</td></tr>
        <tr><td>Tobias Fenwick</td><td>2:20 PM</td><td class="active-state">Still active</td></tr>
        <tr><td>Priya Aldana Rowe</td><td>4:40 PM</td><td class="active-state">Still active</td></tr>
        <tr><td>Owen Brackley</td><td>4:32 PM</td><td class="active-state">Still active</td></tr>
        <tr><td>Lena Marsh</td><td>3:20 PM</td><td class="active-state">Still active</td></tr>
        <tr><td>Tobias Fenwick</td><td>2:20 PM</td><td class="active-state">Still active</td></tr>
        <tr><td>Priya Aldana Rowe</td><td>4:40 PM</td><td class="active-state">Still active</td></tr>
        <tr><td>Lena Marsh</td><td>3:20 PM</td><td class="active-state">Still active</td></tr>
        <tr><td>Tobias Fenwick</td><td>2:20 PM</td><td class="active-state">Still active</td></tr>
        <tr><td>Priya Aldana Rowe</td><td>4:40 PM</td><td class="active-state">Still active</td></tr>
      </tbody>
    </table>
  </section>
</div>
</body>
</html>
```